Electrical Contracting business card design

We need a simple business card design for an Electrical Contracting business. A simple design would be appreciated
This company has 2 directors so on one it would have Dale Morrow & another with Shane Morrow.
Updates

Project Deadline Extended
Reason: Hello A few designers have asked for a logo unfortunately we don't have one so have extended deadline to see who can help us out with this. CHEERS

Project Deadline Extended
Reason: Waiting for business partner to return from xmas break. cheers

Industry/Entity Type

Business

Contact Information for Business Card

Quolvin Electrical Services P/L
REC: 63417
Residential Commercial Industrial
Service-Repairs-Renovations-Installations-Telephone-Data
Dale Morrow-Ph: 0437 612 388
Email: dale@quolvinelectrical.com.au

Requirements
Should not have
• The design should not have any electrical appliances in it ie: power-points, leads, houses etc.

```html
<!DOCTYPE html>
<html lang="en">
<head>
<meta charset="utf-8">
<title>Quolvin Electrical Services – Business Cards</title>
<link rel="stylesheet" href="https://fonts.googleapis.com/css2?family=Roboto:wght@300;400&display=swap">
<style>
  :root {
    --stage: #646464;
    --card: #ffffff;
    --teal: #23968a;
    --teal-dark: #2c7c78;
    --ink: #353535;
    --orange: #e8743b;
    --band-text: #ffffff;
  }
  * { margin: 0; padding: 0; box-sizing: border-box; }
  html, body {
    width: 1200px; height: 1085px; overflow: hidden;
    background: var(--stage);
    font-family: "Roboto", Arial, sans-serif;
    font-weight: 300;
  }
  .canvas { position: relative; width: 1200px; height: 1085px; }
  .card {
    position: absolute; left: 13px; width: 799px; height: 493px;
    background: var(--card); overflow: hidden;
  }
  .card--front { top: 13px; }
  .card--back { top: 532px; }
  .line {
    position: absolute; left: 0; width: 100%;
    text-align: center; line-height: 1; white-space: nowrap;
  }
  .brand-mark {
    position: absolute; left: 0; width: 100%;
    display: flex; justify-content: center; align-items: center; gap: 14px;
    color: var(--orange); font-weight: 400; letter-spacing: 3px; line-height: 1;
  }
  .brand-mark__dot { border-radius: 50%; background: var(--orange); }
  .card--front .brand-mark { top: 112px; font-size: 34px; }
  .card--front .brand-mark__dot { width: 26px; height: 26px; }
  .card--back .brand-mark { top: 203px; font-size: 22px; }
  .card--back .brand-mark__dot { width: 16px; height: 16px; }
  .rule { position: absolute; height: 2px; background: var(--orange); }
  .rule--front { left: 143px; width: 512px; top: 210px; }
  .rule--back {
    left: 251px; width: 288px; top: 257px;
    background: linear-gradient(90deg, rgba(232,116,59,0), var(--orange) 25%, var(--orange) 75%, rgba(232,116,59,0));
  }
  .company-name { top: 228px; font-size: 34px; color: var(--ink); letter-spacing: 1.5px; }
  .services { top: 263px; font-size: 18px; color: var(--teal); letter-spacing: 1.2px; }
  .details { top: 415px; font-size: 14px; color: var(--ink); font-weight: 400; letter-spacing: 1px; }
  .email-band {
    position: absolute; left: 0; top: 440px; width: 100%; height: 24px;
    background: var(--teal); color: var(--band-text);
    text-align: center; font-size: 18px; line-height: 24px;
    font-weight: 400; letter-spacing: 1.5px;
  }
  .back-heading { font-size: 19px; color: var(--teal-dark); letter-spacing: 1.3px; font-weight: 400; }
  .back-heading--one { top: 32px; }
  .back-heading--two { top: 58px; }
  .person-name { top: 277px; font-size: 30px; color: var(--teal-dark); letter-spacing: 1.5px; font-weight: 400; }
  .infoline { top: 316px; font-size: 16px; color: var(--teal); letter-spacing: 1.3px; font-weight: 400; }
  .stage-mark {
    position: absolute; left: 888px; top: 947px; width: 200px;
    display: flex; justify-content: center; align-items: center; gap: 12px;
    color: var(--orange); font-size: 30px; font-weight: 400; letter-spacing: 3px; line-height: 1;
  }
  .stage-mark .brand-mark__dot { width: 22px; height: 22px; }
  .stage-rule { position: absolute; left: 0; top: 1050px; width: 1200px; height: 3px; background: var(--orange); }
</style>
</head>
<body>
<main class="canvas">
  <section class="card card--front" aria-label="Business card front">
    <div class="brand-mark"><span class="brand-mark__dot"></span>QUOLVIN</div>
    <div class="rule rule--front"></div>
    <p class="line company-name">QUOLVIN ELECTRICAL SERVICES</p>
    <p class="line services">REPAIRS-RENOVATIONS-INSTALLATIONS-TELEPHONE</p>
    <p class="line details">P / L REC : 63417&nbsp; RESIDENTIAL COMMERCIAL INDUSTRIAL DATA DALE MORROW - PH: 0437 612 388</p>
    <p class="email-band">EMAIL: DALE@QUOLVINELECTRICAL.COM.AU</p>
  </section>

  <section class="card card--back" aria-label="Business card back">
    <p class="line back-heading back-heading--one">QUOLVIN ELECTRICAL SERVICES&nbsp; RESIDENTIAL&nbsp; COMMERCIAL INDUSTRIAL</p>
    <p class="line back-heading back-heading--two">P/L REC: 63417 REPAIRS - RENOVATIONS - INSTALLATIONS - TELEPHONE</p>
    <div class="brand-mark"><span class="brand-mark__dot"></span>QUOLVIN</div>
    <div class="rule rule--back"></div>
    <p class="line person-name">DALE MORROW</p>
    <p class="line infoline">INFOLINE 0437 612 388</p>
    <p class="email-band">EMAIL: DALE@QUOLVINELECTRICAL.COM.AU</p>
  </section>

  <div class="stage-mark"><span class="brand-mark__dot"></span>QUOLVIN</div>
  <div class="stage-rule"></div>
</main>
</body>
</html>
```